Label design for our new range of organic honey.

We need a design for honey jars and tubs. The label needs to indicate we are located in the Western Australia. The design needs to be elegant, modern and attracting high end customers that focus on quality.

Need extra days to review

```html
<!DOCTYPE html>
<html lang="en">
<head>
<meta charset="utf-8">
<title>Australian Jarrah Raw Honey – Jar Label</title>
<link rel="stylesheet" href="https://fonts.googleapis.com/css2?family=Hind:wght@400;500;600;700&display=swap">
<style>
  :root {
    --page-bg: #ffffff;
    --honey-light: #c8713a;
    --honey-mid: #a8511f;
    --honey-deep: #6e2c0c;
    --gold: #f7e43a;
    --white: #ffffff;
    --seal-black: #111111;
    --seal-comb: #2a2a14;
  }
  html, body {
    margin: 0;
    padding: 0;
    width: 1200px;
    height: 1200px;
    overflow: hidden;
    background: var(--page-bg);
  }
  .canvas {
    position: relative;
    width: 1200px;
    height: 1200px;
    background: var(--page-bg);
  }
  .label {
    position: absolute;
    left: 150px;
    top: 150px;
    width: 900px;
    height: 900px;
    border-radius: 18px;
    overflow: hidden;
    background:
      radial-gradient(ellipse at 55% 60%, rgba(210,120,60,0.55) 0%, rgba(210,120,60,0) 55%),
      linear-gradient(180deg, var(--honey-deep) 0%, var(--honey-mid) 40%, var(--honey-light) 75%, var(--honey-mid) 100%);
    font-family: "Hind", "Segoe UI", sans-serif;
  }
  .seal-strip {
    position: absolute;
    left: 0;
    top: 0;
    width: 110px;
    height: 760px;
    background: var(--seal-black);
  }
  .seal-pattern {
    position: absolute;
    inset: 0;
    background: linear-gradient(90deg, var(--seal-black) 0%, var(--seal-comb) 50%, var(--seal-black) 100%);
  }
  .seal-text {
    position: absolute;
    left: 0;
    bottom: 20px;
    width: 110px;
    height: 720px;
    writing-mode: vertical-rl;
    transform: rotate(180deg);
    display: flex;
    align-items: center;
    justify-content: flex-start;
    color: var(--gold);
    font-weight: 500;
    font-size: 62px;
    letter-spacing: 2px;
    white-space: nowrap;
  }
  .copy {
    position: absolute;
    left: 200px;
    top: 250px;
    width: 680px;
  }
  .origin-kicker {
    color: var(--gold);
    font-weight: 500;
    font-size: 40px;
    line-height: 1;
    letter-spacing: 1px;
    margin: 0;
  }
  .variety {
    color: var(--gold);
    font-weight: 700;
    font-size: 128px;
    line-height: 1;
    letter-spacing: 3px;
    margin: 24px 0 0;
  }
  .claim, .product {
    color: var(--white);
    margin: 26px 0 0;
    line-height: 1;
    display: flex;
    align-items: baseline;
  }
  .claim .big, .product .big {
    font-weight: 700;
    font-size: 86px;
  }
  .claim .small, .product .small {
    font-weight: 600;
    font-size: 52px;
  }
  .claim .small { margin-left: 22px; }
  .product .big { margin-left: 40px; letter-spacing: 2px; }
  .origin-line {
    color: var(--gold);
    font-weight: 400;
    font-size: 50px;
    line-height: 1;
    margin: 66px 0 0;
  }
  .net-weight {
    color: var(--white);
    font-weight: 400;
    font-size: 40px;
    line-height: 1;
    margin: 80px 0 0;
  }
</style>
</head>
<body>
  <div class="canvas">
    <section class="label">
      <div class="seal-strip">
        <div class="seal-pattern" role="img" aria-label="Fine gold honeycomb pattern on black seal strip"></div>
        <div class="seal-text">RAW ORGANIC RA</div>
      </div>
      <div class="copy">
        <p class="origin-kicker">AUSTRALIAN</p>
        <h1 class="variety">JARRAH</h1>
        <p class="claim"><span class="big">100%</span><span class="small">ORGANIC</span></p>
        <p class="product"><span class="small">RAW</span><span class="big">HONEY</span></p>
        <p class="origin-line">Sourced from Western Australia</p>
        <p class="net-weight">500 gms</p>
      </div>
    </section>
  </div>
</body>
</html>
```